Brindle Logistics Business Card Design

We are a trucking and warehousing company. We run freight in the US manly from the Pacific NW to TX and back up the the PNW. We also do warehousing where we store, move, and distribute freight. Looking for a clean and modern design of business card. We would like to look rich and elegant. Attached is our logo.

Industry/Entity Type

Trucking Company

Contact Information for Business Card

Looking for a clean and modern design of business card. We would like to look rich and elegant.

Font styles to use
Sans Serif

Colors

Designer to choose colors to be used in the design.

Requirements
Must have
• logo but it should not dominate the card
Should not have
• logo should not dominate the card

```html
<!DOCTYPE html>
<html lang="en">
<head>
<meta charset="utf-8">
<title>Brindle Logistics Business Card</title>
<link rel="stylesheet" href="https://fonts.googleapis.com/css2?family=Michroma&family=Roboto:wght@400;500&display=swap">
<style>
  :root {
    --backdrop: #2b2b2d;
    --card-black: #0b0b0c;
    --brand-blue: #1b73bd;
    --accent-orange: #f39a1e;
    --paper-white: #ffffff;
    --ink-grey: #5d5f63;
  }
  * { margin: 0; padding: 0; box-sizing: border-box; }
  html, body { width: 1200px; height: 864px; overflow: hidden; background: var(--backdrop); }
  .canvas { position: relative; width: 1200px; height: 864px; }

  .card {
    position: absolute;
    width: 560px;
    height: 320px;
    border-radius: 4px;
    overflow: hidden;
    box-shadow: 0 14px 30px rgba(0,0,0,.45);
  }

  /* Back side */
  .card-back { left: 80px; top: 80px; background: var(--card-black); }
  .card-back .wordmark {
    position: absolute; left: 0; right: 0; top: 50%;
    transform: translateY(-50%);
    display: flex; align-items: center; justify-content: center; gap: 16px;
  }
  .wordmark-dot { width: 18px; height: 18px; border-radius: 50%; background: var(--brand-blue); flex: none; }
  .wordmark-text {
    font-family: "Michroma", sans-serif;
    font-size: 26px; letter-spacing: 2px;
    color: var(--paper-white);
  }

  /* Front side */
  .card-front { left: 560px; top: 464px; background: var(--paper-white); }
  .front-field { position: absolute; inset: 0; }
  .holder {
    position: absolute; left: 30px; top: 40px;
    color: var(--paper-white);
  }
  .holder-name {
    font-family: "Michroma", sans-serif;
    font-size: 20px; font-weight: 400; letter-spacing: 1px;
  }
  .holder-title {
    font-family: "Michroma", sans-serif;
    font-size: 10.5px; letter-spacing: 1.5px; margin-top: 2px;
  }
  .holder-address {
    font-family: "Roboto", sans-serif;
    font-size: 13px; line-height: 1.4; margin-top: 14px;
  }
  .contact-list {
    position: absolute; left: 30px; bottom: 26px;
    list-style: none;
    font-family: "Roboto", sans-serif; font-size: 15px; color: var(--paper-white);
  }
  .contact-list li { display: flex; align-items: center; gap: 10px; line-height: 1.55; }
  .contact-icon { width: 14px; height: 14px; flex: none; }

  .card-front .wordmark {
    position: absolute; right: 28px; bottom: 66px;
    display: flex; align-items: center; gap: 10px;
  }
  .card-front .wordmark-text {
    color: var(--ink-grey); font-size: 18px; letter-spacing: 1.5px; line-height: 1.3;
  }
  .card-front .wordmark-dot { width: 12px; height: 12px; }
</style>
</head>
<body>
<main class="canvas">

  <section class="card card-back" aria-label="Card back">
    <div class="wordmark">
      <span class="wordmark-dot"></span>
      <span class="wordmark-text">BRINDLE LOGISTICS</span>
    </div>
  </section>

  <section class="card card-front" aria-label="Card front">
    <svg class="front-field" viewBox="0 0 560 320" preserveAspectRatio="none" role="img" aria-label="Blue field where the large bird head artwork belongs">
      <path d="M0 0 H230 C300 20 340 80 330 150 C322 220 330 280 360 320 H0 Z" fill="var(--brand-blue)"/>
      <path d="M230 0 C300 20 340 80 330 150 C322 220 330 280 360 320" fill="none" stroke="var(--paper-white)" stroke-width="6"/>
    </svg>

    <div class="holder">
      <h1 class="holder-name">DANA WHITLOW</h1>
      <p class="holder-title">MANAGING DIRECTOR</p>
      <p class="holder-address">48 Alder Creek Road<br>RM of Marlow, Easton<br>Saskatchewan, S7T 2B9</p>
    </div>

    <ul class="contact-list">
      <li>
        <svg class="contact-icon" viewBox="0 0 16 16"><path d="M4 1l3 3-2 2c1 2 3 4 5 5l2-2 3 3-2 3C7 15 1 9 1 3z" fill="var(--accent-orange)"/></svg>
        306.555.0148
      </li>
      <li>
        <svg class="contact-icon" viewBox="0 0 16 16"><rect x="1" y="3" width="14" height="10" fill="var(--accent-orange)"/><path d="M1 3l7 6 7-6" fill="none" stroke="var(--brand-blue)" stroke-width="1.3"/></svg>
        info@brindlelogistics.com
      </li>
      <li>
        <svg class="contact-icon" viewBox="0 0 16 16" fill="none" stroke="var(--accent-orange)" stroke-width="1.4"><circle cx="8" cy="8" r="6.5"/><ellipse cx="8" cy="8" rx="3" ry="6.5"/><path d="M1.5 8h13M3 4.5h10M3 11.5h10"/></svg>
        www.brindlelogistics.com
      </li>
    </ul>

    <div class="wordmark">
      <span class="wordmark-dot"></span>
      <span class="wordmark-text">BRINDLE<br>LOGISTICS</span>
    </div>
  </section>

</main>
</body>
</html>
```